Modern design for a watersports website

Building a brand new site for Kiteboarders/Kitesurfers .... this is the first of 8 sites we're rolling out.

We're as much looking for a partner to work with, and they will be chosen based on the winner of this site design.

It will need these menu pages:

1) How-To
2) Classifieds
3) Groups
4) News
5) Events

Width: 1150px

The home page, should feature:

1) A search box to enter a location
2) Under that, a series of boxes showing up to 5 previous locations chosen - these should be "buttons", directly under the location (i.e. no photo, just the location name)
3) Under that, a 5 x 3 grid of adverts, featuring a photo, a title & a price
4) Under that, top 5 headlines, each one featuring photo, headline & Summary
5) Under that, top 10 Group topics: Group, Title, Author, #Replies (no photo for these)
6) Under that, 5 x 3 grid of photos
7) Footer

Colours should be of the ocean:
Blues, greens, compatible with yellow. (i.e. not washed out blues like tessaloom), vibrant blues, but not too vivid as to overpower.

Avoid: Photos of any equipment, as they will date quickly.

Industry/Entity Type

Building

Number of Pages Required

1 page

Font styles to use
Sans Serif

Requirements
Must have
• Ocean colours; blues
Nice to have
• Modern design

```html
<!DOCTYPE html>
<html lang="en">
<head>
<meta charset="utf-8">
<title>Kite Boarder</title>
<link href="https://fonts.googleapis.com/css2?family=Source+Sans+3:wght@300;400;600;700&display=swap" rel="stylesheet">
<style>
:root{
  --ocean:#1f9fd6;
  --ocean-deep:#1486c0;
  --teal:#2aa7c9;
  --green:#7cc242;
  --ink:#555b61;
  --muted:#8a9096;
  --line:#e4e7ea;
  --page:#f6f7f8;
  --white:#ffffff;
}
*{box-sizing:border-box;margin:0;padding:0}
html,body{width:1200px;height:4905px;overflow:hidden}
body{font-family:"Source Sans 3",Arial,sans-serif;color:var(--ink);background:var(--white)}

/* hero */
.hero{position:relative;height:540px;overflow:hidden}
.hero-photo{position:absolute;inset:0;background:linear-gradient(180deg,#9cc3df 0%,#c9dceb 30%,#5fb6c8 55%,#2a8fb0 70%,#d9c9a4 86%,#c8b58d 100%)}
.hero-shade{position:absolute;inset:0;background:linear-gradient(180deg,rgba(0,0,0,.25),rgba(0,0,0,0) 25%)}
.main-nav{position:absolute;top:22px;left:0;right:0;display:flex;justify-content:center;gap:40px}
.main-nav a{color:var(--white);font-size:14px;letter-spacing:1px;text-decoration:none}
.site-title{position:absolute;top:148px;width:100%;text-align:center;color:var(--white);font-size:56px;font-weight:700;letter-spacing:2px}
.title-rule{position:absolute;top:228px;left:570px;width:60px;height:2px;background:var(--white)}
.search-panel{position:absolute;top:282px;left:303px;width:594px;height:140px;background:rgba(255,255,255,.92);padding:18px}
.search-row{display:flex;gap:6px}
.search-input{flex:1;height:40px;border:1px solid var(--line);background:var(--white);font-size:13px;color:var(--muted);padding:11px 14px}
.search-btn{width:92px;height:40px;background:var(--ocean);color:var(--white);font-size:13px;font-weight:600;text-align:center;line-height:40px}
.recent{display:flex;gap:12px;margin-top:20px}
.recent span{width:104px;height:36px;border:1px solid var(--line);border-radius:18px;background:var(--white);font-size:12px;color:var(--muted);display:flex;align-items:center;padding-left:14px;gap:8px}
.recent span::before{content:"";width:10px;height:10px;border:1px solid #c5cace;border-radius:50%}
.recent span.active{background:var(--green);color:var(--white);border-color:var(--green)}
.recent span.active::before{background:var(--white);border-color:var(--white)}
.hero-dots{position:absolute;top:470px;left:0;right:0;display:flex;justify-content:center;gap:10px}
.hero-dots i{width:10px;height:10px;border-radius:50%;background:rgba(255,255,255,.6)}
.hero-dots i:first-child{background:var(--white)}

/* sections */
.section-title{text-align:center;font-size:26px;font-weight:300;letter-spacing:1px;text-transform:uppercase}
.section-title::after{content:"";display:block;width:60px;height:2px;margin:18px auto 0;background:currentColor;opacity:.6}

.adverts{height:1620px;background:linear-gradient(160deg,#27aee3 0%,var(--ocean) 50%,var(--ocean-deep) 100%);padding-top:56px;color:var(--white)}
.advert-grid{width:800px;margin:44px auto 0;display:grid;grid-template-columns:repeat(3,240px);column-gap:40px;row-gap:38px}
.advert-card{height:250px;background:var(--white);text-align:center;color:var(--ink)}
.advert-photo{height:130px;background:linear-gradient(135deg,#f07a2a,#2f6fb5 55%,#e9b04a)}
.card-name{color:var(--teal);font-size:16px;font-weight:400;margin-top:14px;text-transform:uppercase}
.card-text{font-size:11px;line-height:15px;color:var(--muted);padding:4px 24px 0}
.price{color:var(--green);font-size:24px;font-style:italic;font-weight:600;margin-top:4px}

.headlines{height:840px;padding-top:56px;background:var(--white)}
.headline-grid{width:800px;margin:40px auto 0;display:flex;flex-wrap:wrap;justify-content:center;gap:38px 40px}
.headline-card{width:240px;height:290px;background:var(--white);border:1px solid var(--line);text-align:center}
.headline-photo{height:130px;background:linear-gradient(180deg,#1e7fc8,#2aa3da 50%,#1a6fae)}
.headline-card .card-text{padding:6px 18px 0}
.read-more{display:inline-block;margin-top:12px;width:76px;height:26px;line-height:26px;background:var(--ocean);color:var(--white);font-size:10px;font-weight:600}

.topics{height:378px;padding-top:56px;background:var(--page);position:relative}
.topic-row{width:800px;margin:40px auto 0;display:grid;grid-template-columns:repeat(3,240px);column-gap:40px}
.topic-card{height:164px;background:var(--white);border:1px solid var(--line);text-align:center}
.topic-title{color:var(--teal);font-size:16px;margin-top:22px;text-transform:uppercase}
.topic-author{color:var(--green);font-size:11px;margin-top:4px;text-transform:uppercase}
.topic-text{font-size:11px;line-height:15px;color:var(--muted);padding:8px 20px 0;height:56px}
.topic-meta{display:flex;justify-content:space-between;border-top:1px solid var(--line);padding:10px 16px;font-size:11px;color:var(--muted)}
.topic-meta span{display:flex;align-items:center;gap:5px}
.arrow{position:absolute;top:222px}
.arrow.prev{left:168px}.arrow.next{left:1010px}

.gallery{height:1125px;padding-top:56px;background:var(--white)}
.gallery-grid{width:800px;margin:44px auto 0;display:grid;grid-template-columns:repeat(3,1fr);grid-auto-rows:181px}
.tile{position:relative}
.tile.swim{background:linear-gradient(180deg,#1b7dc5,#2aa7e0 55%,#176fb0)}
.tile.sail{background:linear-gradient(180deg,#6fb1e0,#cfe3f2 45%,#3fa9c5 65%,#d8c7a0)}
.tile.splash{background:linear-gradient(135deg,#2b5c7c,#c4743e 50%,#9fd2ea)}
.tile.hover{background:#2b3238}
.tile.hover svg{position:absolute;left:117px;top:68px}

.newsletter{height:183px;background:var(--ocean);color:var(--white);padding-top:36px}
.newsletter .section-title{font-size:22px}
.newsletter .section-title::after{margin-top:12px;width:50px}
.subscribe{display:flex;justify-content:center;margin-top:24px}
.subscribe .field{width:244px;height:34px;background:var(--white);font-size:11px;color:var(--muted);padding:10px 12px}
.subscribe .go{width:90px;height:34px;background:#d7dde2;color:var(--white);font-size:11px;line-height:34px;text-align:center}

.footer{height:219px;background:var(--white);text-align:center;padding-top:36px}
.partners{display:flex;justify-content:center;align-items:center;gap:44px}
.partners i{display:block;background:#c9ced3}
.partners .sq{width:46px;height:38px}
.partners .ci{width:40px;height:40px;border-radius:50%}
.social{display:flex;justify-content:center;gap:18px;margin-top:28px;font-size:11px;color:var(--ink)}
.social span{display:flex;align-items:center;gap:5px}
.social span::before{content:"";width:14px;height:14px;border-radius:50%;background:#3a4047}
.foot-links{display:flex;justify-content:center;gap:16px;margin-top:14px;font-size:10px;color:var(--muted)}
.copyright{font-size:10px;color:var(--muted);margin-top:6px}
</style>
</head>
<body>

<header class="hero">
  <div class="hero-photo" role="img" aria-label="Parasail over a tropical beach with people running on the sand"></div>
  <div class="hero-shade"></div>
  <nav class="main-nav"><a>HOME</a><a>HOW TO</a><a>CLASSIFIEDS</a><a>GROUPS</a><a>NEWS</a><a>EVENTS</a></nav>
  <h1 class="site-title">KITE BOARDER</h1>
  <div class="title-rule"></div>
  <div class="search-panel">
    <div class="search-row"><div class="search-input">Enter your location</div><div class="search-btn">SEARCH</div></div>
    <div class="recent"><span class="active">Noosa</span><span>Byron</span><span>Manly</span><span>Phuket</span><span>Torquay</span></div>
  </div>
  <div class="hero-dots"><i></i><i></i></div>
</header>

<section class="adverts">
  <h2 class="section-title">Advert</h2>
  <div class="advert-grid">
    <article class="advert-card"><div class="advert-photo" role="img" aria-label="Rowers paddling together"></div><h3 class="card-name">Project Name</h3><p class="card-text">Lorem ipsum dolor sit amet, consectetur adipiscing elit. Proin sapien.</p><p class="price">$250</p></article>
    <article class="advert-card"><div class="advert-photo" role="img" aria-label="Rowers paddling together"></div><h3 class="card-name">Project Name</h3><p class="card-text">Lorem ipsum dolor sit amet, consectetur adipiscing elit. Proin sapien.</p><p class="price">$250</p></article>
    <article class="advert-card"><div class="advert-photo" role="img" aria-label="Rowers paddling together"></div><h3 class="card-name">Project Name</h3><p class="card-text">Lorem ipsum dolor sit amet, consectetur adipiscing elit. Proin sapien.</p><p class="price">$250</p></article>
    <article class="advert-card"><div class="advert-photo" role="img" aria-label="Rowers paddling together"></div><h3 class="card-name">Project Name</h3><p class="card-text">Lorem ipsum dolor sit amet, consectetur adipiscing elit. Proin sapien.</p><p class="price">$250</p></article>
    <article class="advert-card"><div class="advert-photo" role="img" aria-label="Rowers paddling together"></div><h3 class="card-name">Project Name</h3><p class="card-text">Lorem ipsum dolor sit amet, consectetur adipiscing elit. Proin sapien.</p><p class="price">$250</p></article>
    <article class="advert-card"><div class="advert-photo" role="img" aria-label="Rowers paddling together"></div><h3 class="card-name">Project Name</h3><p class="card-text">Lorem ipsum dolor sit amet, consectetur adipiscing elit. Proin sapien.</p><p class="price">$250</p></article>
    <article class="advert-card"><div class="advert-photo" role="img" aria-label="Rowers paddling together"></div><h3 class="card-name">Project Name</h3><p class="card-text">Lorem ipsum dolor sit amet, consectetur adipiscing elit. Proin sapien.</p><p class="price">$250</p></article>
    <article class="advert-card"><div class="advert-photo" role="img" aria-label="Rowers paddling together"></div><h3 class="card-name">Project Name</h3><p class="card-text">Lorem ipsum dolor sit amet, consectetur adipiscing elit. Proin sapien.</p><p class="price">$250</p></article>
    <article class="advert-card"><div class="advert-photo" role="img" aria-label="Rowers paddling together"></div><h3 class="card-name">Project Name</h3><p class="card-text">Lorem ipsum dolor sit amet, consectetur adipiscing elit. Proin sapien.</p><p class="price">$250</p></article>
    <article class="advert-card"><div class="advert-photo" role="img" aria-label="Rowers paddling together"></div><h3 class="card-name">Project Name</h3><p class="card-text">Lorem ipsum dolor sit amet, consectetur adipiscing elit. Proin sapien.</p><p class="price">$250</p></article>
    <article class="advert-card"><div class="advert-photo" role="img" aria-label="Rowers paddling together"></div><h3 class="card-name">Project Name</h3><p class="card-text">Lorem ipsum dolor sit amet, consectetur adipiscing elit. Proin sapien.</p><p class="price">$250</p></article>
    <article class="advert-card"><div class="advert-photo" role="img" aria-label="Rowers paddling together"></div><h3 class="card-name">Project Name</h3><p class="card-text">Lorem ipsum dolor sit amet, consectetur adipiscing elit. Proin sapien.</p><p class="price">$250</p></article>
    <article class="advert-card"><div class="advert-photo" role="img" aria-label="Rowers paddling together"></div><h3 class="card-name">Project Name</h3><p class="card-text">Lorem ipsum dolor sit amet, consectetur adipiscing elit. Proin sapien.</p><p class="price">$250</p></article>
    <article class="advert-card"><div class="advert-photo" role="img" aria-label="Rowers paddling together"></div><h3 class="card-name">Project Name</h3><p class="card-text">Lorem ipsum dolor sit amet, consectetur adipiscing elit. Proin sapien.</p><p class="price">$250</p></article>
    <article class="advert-card"><div class="advert-photo" role="img" aria-label="Rowers paddling together"></div><h3 class="card-name">Project Name</h3><p class="card-text">Lorem ipsum dolor sit amet, consectetur adipiscing elit. Proin sapien.</p><p class="price">$250</p></article>
  </div>
</section>

<section class="headlines">
  <h2 class="section-title">Top 5 Headlines</h2>
  <div class="headline-grid">
    <article class="headline-card"><div class="headline-photo" role="img" aria-label="Swimmer racing in a pool lane"></div><h3 class="card-name">Project Name</h3><p class="card-text">Lorem ipsum dolor sit amet, consectetur adipiscing elit. Morbi eget ante quam. Nunc rutrum tellus, quis pretium felis tincidunt vitae. Duis at odio nec augue porta.</p><span class="read-more">READ MORE</span></article>
    <article class="headline-card"><div class="headline-photo" role="img" aria-label="Swimmer racing in a pool lane"></div><h3 class="card-name">Project Name</h3><p class="card-text">Lorem ipsum dolor sit amet, consectetur adipiscing elit. Morbi eget ante quam. Nunc rutrum tellus, quis pretium felis tincidunt vitae. Duis at odio nec augue porta.</p><span class="read-more">READ MORE</span></article>
    <article class="headline-card"><div class="headline-photo" role="img" aria-label="Swimmer racing in a pool lane"></div><h3 class="card-name">Project Name</h3><p class="card-text">Lorem ipsum dolor sit amet, consectetur adipiscing elit. Morbi eget ante quam. Nunc rutrum tellus, quis pretium felis tincidunt vitae. Duis at odio nec augue porta.</p><span class="read-more">READ MORE</span></article>
    <article class="headline-card"><div class="headline-photo" role="img" aria-label="Swimmer racing in a pool lane"></div><h3 class="card-name">Project Name</h3><p class="card-text">Lorem ipsum dolor sit amet, consectetur adipiscing elit. Morbi eget ante quam. Nunc rutrum tellus, quis pretium felis tincidunt vitae. Duis at odio nec augue porta.</p><span class="read-more">READ MORE</span></article>
    <article class="headline-card"><div class="headline-photo" role="img" aria-label="Swimmer racing in a pool lane"></div><h3 class="card-name">Project Name</h3><p class="card-text">Lorem ipsum dolor sit amet, consectetur adipiscing elit. Morbi eget ante quam. Nunc rutrum tellus, quis pretium felis tincidunt vitae. Duis at odio nec augue porta.</p><span class="read-more">READ MORE</span></article>
  </div>
</section>

<section class="topics">
  <h2 class="section-title">Top 10 Group Topics</h2>
  <svg class="arrow prev" width="20" height="30" viewBox="0 0 20 30"><path d="M15 3 L4 15 L15 27" fill="none" stroke="#cfd4d8" stroke-width="3"/></svg>
  <svg class="arrow next" width="20" height="30" viewBox="0 0 20 30"><path d="M5 3 L16 15 L5 27" fill="none" stroke="#2aa7c9" stroke-width="3"/></svg>
  <div class="topic-row">
    <article class="topic-card"><h3 class="topic-title">Title of the Topic</h3><p class="topic-author">By Alex Reed</p><p class="topic-text">Lorem ipsum dolor sit amet, consectetur adipiscing elit. Proin sapien nibh, varius at felis.</p><div class="topic-meta"><span><svg width="12" height="11" viewBox="0 0 12 11"><path d="M1 1h10v7H5l-3 3V8H1z" fill="#2aa7c9"/></svg>8 comments</span><span><svg width="12" height="11" viewBox="0 0 12 11"><path d="M6 10 1 5a2.6 2.6 0 0 1 5-3 2.6 2.6 0 0 1 5 3z" fill="#2aa7c9"/></svg>5 likes</span></div></article>
    <article class="topic-card"><h3 class="topic-title">Title of the Topic</h3><p class="topic-author">By Alex Reed</p><p class="topic-text">Lorem ipsum dolor sit amet, consectetur adipiscing elit. Proin sapien nibh, varius at felis.</p><div class="topic-meta"><span><svg width="12" height="11" viewBox="0 0 12 11"><path d="M1 1h10v7H5l-3 3V8H1z" fill="#2aa7c9"/></svg>8 comments</span><span><svg width="12" height="11" viewBox="0 0 12 11"><path d="M6 10 1 5a2.6 2.6 0 0 1 5-3 2.6 2.6 0 0 1 5 3z" fill="#2aa7c9"/></svg>5 likes</span></div></article>
    <article class="topic-card"><h3 class="topic-title">Title of the Topic</h3><p class="topic-author">By Alex Reed</p><p class="topic-text">Lorem ipsum dolor sit amet, consectetur adipiscing elit. Proin sapien nibh, varius at felis.</p><div class="topic-meta"><span><svg width="12" height="11" viewBox="0 0 12 11"><path d="M1 1h10v7H5l-3 3V8H1z" fill="#2aa7c9"/></svg>8 comments</span><span><svg width="12" height="11" viewBox="0 0 12 11"><path d="M6 10 1 5a2.6 2.6 0 0 1 5-3 2.6 2.6 0 0 1 5 3z" fill="#2aa7c9"/></svg>5 likes</span></div></article>
  </div>
</section>

<section class="gallery">
  <h2 class="section-title">Photo Gallery</h2>
  <div class="gallery-grid">
    <div class="tile swim" role="img" aria-label="Swimmer in a pool"></div>
    <div class="tile hover" role="img" aria-label="Water splash photo with zoom overlay"><svg width="34" height="34" viewBox="0 0 34 34"><circle cx="14" cy="14" r="10" fill="none" stroke="#7cc242" stroke-width="3"/><path d="M21 21 31 31" stroke="#7cc242" stroke-width="4" stroke-linecap="round"/></svg></div>
    <div class="tile sail" role="img" aria-label="Parasail over the beach"></div>
    <div class="tile sail" role="img" aria-label="Parasail over the beach"></div>
    <div class="tile splash" role="img" aria-label="Swimmer splashing"></div>
    <div class="tile swim" role="img" aria-label="Swimmer in a pool"></div>
    <div class="tile swim" role="img" aria-label="Swimmer in a pool"></div>
    <div class="tile splash" role="img" aria-label="Swimmer splashing"></div>
    <div class="tile sail" role="img" aria-label="Parasail over the beach"></div>
    <div class="tile sail" role="img" aria-label="Parasail over the beach"></div>
    <div class="tile splash" role="img" aria-label="Swimmer splashing"></div>
    <div class="tile swim" role="img" aria-label="Swimmer in a pool"></div>
    <div class="tile swim" role="img" aria-label="Swimmer in a pool"></div>
    <div class="tile splash" role="img" aria-label="Swimmer splashing"></div>
    <div class="tile sail" role="img" aria-label="Parasail over the beach"></div>
  </div>
</section>

<section class="newsletter">
  <h2 class="section-title">Subscribe to our Newsletter</h2>
  <div class="subscribe"><div class="field">Enter your email</div><div class="go">SUBSCRIBE</div></div>
</section>

<footer class="footer">
  <div class="partners"><i class="sq"></i><i class="sq"></i><i class="ci"></i><i class="sq"></i><i class="ci"></i></div>
  <div class="social"><span>tessaloom</span><span>Chirpline</span><span>Vidreel</span></div>
  <nav class="foot-links"><span>Home</span><span>How To</span><span>Classifieds</span><span>Groups</span><span>News</span><span>Events</span></nav>
  <p class="copyright">Copyright © 2015 Kite Boarder. All rights reserved.</p>
</footer>

</body>
</html>
```